Halvern Aviation Group - "Coming Soon" Main Company Webpage

Design a main webpage that can be posted while a fully functional website is constructed. The design should be created to convey a sense of luxury and exclusivity. The main page should contain only one photo as the background. The photo I believe to show "luxury" and "Exclusivity" is listed as "Global Luxury Photo". I have included two other photos as well to aid in providing a variety of presentations.
The "Member PQTR" logo should appear somewhere on the main page but be less prevalent than the main company logo. "Coming Soon" should also appear to convey that a website is being constructed.
Tabs for the website:
- Aircraft Management
- Aircraft Sales
- Pilot Services
- Charter
- Flight Training

```html
<!DOCTYPE html>
<html lang="en">
<head>
<meta charset="utf-8">
<title>Halvern Aviation Group – Coming Soon</title>
<link rel="stylesheet" href="https://fonts.googleapis.com/css2?family=Roboto:wght@300;400;500&display=swap">
<style>
  :root {
    --sky-top: #8fc3ec;
    --sky-haze: #d6e2ea;
    --sea: #3f98b8;
    --sea-deep: #2c86a8;
    --sand: #cdb99a;
    --sand-light: #ddd0b8;
    --ink: #111111;
    --brand-blue: #1e6fc0;
    --footer-bg: rgba(70, 74, 78, 0.72);
    --white: #ffffff;
  }
  * { margin: 0; padding: 0; box-sizing: border-box; }
  html, body { width: 1200px; height: 738px; overflow: hidden; }
  body { font-family: "Roboto", Arial, sans-serif; color: var(--ink); }

  .page { position: relative; width: 1200px; height: 738px; overflow: hidden; }

  .hero-photo {
    position: absolute; inset: 0;
    background:
      radial-gradient(ellipse 620px 420px at 980px 560px, var(--sand) 0%, rgba(205,185,154,0) 70%),
      linear-gradient(100deg, rgba(44,134,168,0.95) 0%, rgba(63,152,184,0.85) 45%, rgba(221,208,184,0.9) 62%, var(--sand-light) 100%),
      linear-gradient(180deg, var(--sky-top) 0%, var(--sky-haze) 30%, var(--sea) 100%);
  }
  .hero-photo::before {
    content: ""; position: absolute; left: 0; right: 0; top: 0; height: 300px;
    background: linear-gradient(180deg, var(--sky-top) 0%, rgba(214,226,234,0.9) 50%, rgba(214,226,234,0) 100%);
  }

  .site-header {
    position: absolute; top: 0; left: 0; right: 0; height: 110px;
    display: flex; align-items: flex-start; justify-content: space-between;
    padding: 0 74px;
  }
  .brand {
    margin-top: 30px; display: flex; align-items: center; gap: 12px;
    color: var(--brand-blue); font-weight: 500; text-decoration: none;
  }
  .brand-mark { width: 16px; height: 16px; border-radius: 50%; background: var(--brand-blue); }
  .brand-name { display: flex; flex-direction: column; text-transform: uppercase; line-height: 1; }
  .brand-name-main { font-size: 46px; letter-spacing: 5px; }
  .brand-name-sub { font-size: 20px; letter-spacing: 4.4px; margin-top: 4px; }

  .main-nav { margin-top: 60px; }
  .main-nav ul { display: flex; list-style: none; gap: 22px; }
  .main-nav a {
    font-size: 13px; font-weight: 400; color: var(--ink);
    text-decoration: none; text-transform: uppercase; letter-spacing: 0.2px;
  }

  .coming-soon {
    position: absolute; left: 70px; top: 290px;
    font-weight: 300; font-size: 104px; line-height: 92px;
    text-transform: uppercase; color: var(--ink); letter-spacing: 1px;
  }

  .site-footer {
    position: absolute; left: 0; right: 0; bottom: 0; height: 56px;
    background: var(--footer-bg); color: var(--white);
    display: flex; align-items: center; padding: 0 74px;
  }
  .copyright { font-size: 12.5px; width: 453px; }
  .social { display: flex; gap: 6px; list-style: none; }
  .social a {
    display: flex; align-items: center; justify-content: center;
    width: 32px; height: 32px; border-radius: 50%;
    border: 1.5px solid var(--white);
  }
  .social svg { width: 14px; height: 14px; fill: var(--white); }
  .membership {
    margin-left: auto; display: flex; align-items: center; gap: 8px;
    color: var(--white); font-weight: 400;
  }
  .membership-mark { width: 40px; height: 26px; border-radius: 50%; background: var(--white); }
  .membership-text { display: flex; flex-direction: column; line-height: 1; }
  .membership-label { font-size: 9px; margin-bottom: 3px; }
  .membership-name { font-size: 24px; letter-spacing: 3px; }
</style>
</head>
<body>
<div class="page">
  <div class="hero-photo" role="img" aria-label="Aerial photo of a white private jet flying over a coastal city with a palm-shaped island and blue sea"></div>

  <header class="site-header">
    <a class="brand" href="#">
      <span class="brand-mark"></span>
      <span class="brand-name">
        <span class="brand-name-main">Halvern</span>
        <span class="brand-name-sub">Aviation Group</span>
      </span>
    </a>
    <nav class="main-nav">
      <ul>
        <li><a href="#">Aircraft Management</a></li>
        <li><a href="#">Aircraft Sales</a></li>
        <li><a href="#">Pilot Services</a></li>
        <li><a href="#">Charter</a></li>
        <li><a href="#">Flight Training</a></li>
      </ul>
    </nav>
  </header>

  <h1 class="coming-soon">Coming<br>Soon</h1>

  <footer class="site-footer">
    <p class="copyright">Copyright © 2023 Halvern Aviation Group.&nbsp; All Right Reserved</p>
    <ul class="social">
      <li><a href="#" aria-label="Message us"><svg viewBox="0 0 16 16"><path d="M2 2h12v9H6l-4 3z"/></svg></a></li>
      <li><a href="#" aria-label="Share"><svg viewBox="0 0 16 16"><path d="M3 8l10-6v12z"/></svg></a></li>
      <li><a href="#" aria-label="Location"><svg viewBox="0 0 16 16"><path d="M8 1a5 5 0 0 1 5 5c0 4-5 9-5 9S3 10 3 6a5 5 0 0 1 5-5zm0 3a2 2 0 1 0 0 4 2 2 0 0 0 0-4z"/></svg></a></li>
      <li><a href="#" aria-label="Watch"><svg viewBox="0 0 16 16"><path d="M5 3l8 5-8 5z"/></svg></a></li>
    </ul>
    <div class="membership">
      <span class="membership-mark"></span>
      <span class="membership-text">
        <span class="membership-label">member of</span>
        <span class="membership-name">PQTR</span>
      </span>
    </div>
  </footer>
</div>
</body>
</html>
```